Loan Company looking to offer special summer loan rate for closed customers

We are wanting to design an A5 Summer Holiday themed leaflet. We would like to offer a 10% Cashback when re-opening their loan account.
The leaflet is aimed at our closed customers. We would like to use bright summer colours. I have uploaded one of our Christmas promotion leaflets for you to include the highlighted information to use in this new project. We have also uploaded some ideas of examples that we have seen online as rough guide.
"10% Cashback on all re-opened accounts in July and August 2023!"

```html
<!DOCTYPE html>
<html lang="en">
<head>
<meta charset="utf-8">
<title>Harbourline Summer Cashback Leaflet</title>
<link href="https://fonts.googleapis.com/css2?family=Bebas+Neue&family=Poppins:wght@400;600;700;800&display=swap" rel="stylesheet">
<style>
  :root {
    --page-bg: #e9eaec;
    --sky-top: #e8234c;
    --sky-mid: #f45a3c;
    --sky-glow: #ffc33a;
    --band-top: #d81f66;
    --band-mid: #b3186e;
    --band-bottom: #5d1a5e;
    --white: #ffffff;
    --soft-pink: #fbe0dc;
    --yellow: #ffe23a;
    --pale-yellow: #fff2ad;
    --gold: #ffd02c;
    --orange-box: #f26a2a;
    --phone-orange: #ff9b1c;
    --dusk-purple: #4a1850;
  }
  * { margin: 0; padding: 0; box-sizing: border-box; }
  html, body { width: 1200px; height: 2824px; overflow: hidden; }
  body { background: var(--page-bg); position: relative; font-family: "Poppins", sans-serif; }

  .leaflet {
    position: absolute; left: 87px; top: 747px;
    width: 1026px; height: 1330px; overflow: hidden;
    background: linear-gradient(180deg, var(--band-top) 0%, var(--band-mid) 50%, var(--band-bottom) 100%);
    box-shadow: 0 6px 18px rgba(0,0,0,0.25);
  }
  .sunset-scene {
    position: absolute; left: 0; top: 0; width: 1026px; height: 565px;
    background:
      radial-gradient(circle at 62% 62%, #fff6b0 0%, var(--sky-glow) 18%, rgba(255,170,60,0.6) 36%, rgba(255,120,60,0) 55%),
      linear-gradient(180deg, var(--sky-top) 0%, var(--sky-mid) 45%, #ff9a45 80%, #ffb45a 100%);
  }
  .dusk-island {
    position: absolute; right: 0; bottom: 0; width: 720px; height: 340px;
    background: linear-gradient(180deg, rgba(74,24,80,0) 0%, rgba(74,24,80,0.55) 40%, var(--dusk-purple) 75%);
  }

  .brand {
    position: absolute; left: 0; width: 100%; top: 120px;
    display: flex; align-items: center; justify-content: center; gap: 18px;
  }
  .brand-dot {
    width: 34px; height: 34px; border-radius: 50%; background: var(--soft-pink);
  }
  .brand-name {
    color: var(--soft-pink);
    font-weight: 600; font-size: 60px; line-height: 1; letter-spacing: 0.5px;
  }

  .offer-headline {
    position: absolute; left: 0; width: 100%; top: 592px;
    text-align: center; color: var(--yellow);
    font-family: "Bebas Neue", sans-serif; font-size: 140px; line-height: 1; letter-spacing: 1px;
  }
  .offer-line {
    position: absolute; left: 0; width: 100%; top: 715px;
    text-align: center; color: var(--pale-yellow);
    font-weight: 700; font-size: 40px; line-height: 1.2;
  }
  .offer-dates {
    position: absolute; left: 0; width: 100%; top: 768px;
    text-align: center; color: var(--gold);
    font-weight: 800; font-size: 52px; line-height: 1.2;
  }
  .legal {
    position: absolute; left: 60px; right: 60px; top: 838px;
    text-align: center; color: var(--white);
    font-size: 22px; line-height: 27px;
  }
  .legal strong { font-weight: 700; }
  .legal p + p { margin-top: 26px; }

  .prize-box {
    position: absolute; left: 78px; top: 1030px; width: 273px; height: 292px;
    background: var(--orange-box);
    padding: 18px 14px 0;
    text-align: center; color: var(--white);
    font-weight: 700; font-size: 21px; line-height: 31px;
  }
  .prize-box .hi { color: var(--gold); }
  .prize-box sup { font-size: 12px; }

  .contact {
    position: absolute; right: 26px; top: 1224px; text-align: right;
  }
  .contact-label { color: var(--gold); font-weight: 700; font-size: 20px; }
  .contact-phone { color: var(--phone-orange); font-weight: 700; font-size: 56px; line-height: 1.1; }
</style>
</head>
<body>
  <main class="leaflet">
    <div class="sunset-scene" role="img" aria-label="Tropical sunset illustration with palm leaves, clouds, birds, a sailboat and a palm island"></div>
    <div class="dusk-island" role="img" aria-label="Purple palm silhouettes with cartoon watermelon and pineapple characters wearing sunglasses"></div>

    <div class="brand">
      <span class="brand-dot"></span>
      <h1 class="brand-name">Harbourline Lending</h1>
    </div>

    <h2 class="offer-headline">10% CASHBACK</h2>
    <p class="offer-line">ON ALL RE-OPENED ACCOUNTS IN</p>
    <p class="offer-dates">JULY &amp; AUGUST 2023!</p>

    <div class="legal">
      <p>Representative example: Loan amount <strong>£150.00</strong> payable over <strong>23 weeks</strong> at<br>
      <strong>£10.50 per week</strong>. Interest is <strong>£91.50</strong> The Total amount payable is <strong>£241.50</strong>.<br>
      Interest rate is <strong>138.29%</strong> per annum (fixed). <strong>838.39%</strong> APR representative.</p>
      <p>Terms and conditions apply. All credit is subject to status &amp; affordability.<br>
      Written quotations on request.</p>
    </div>

    <div class="prize-box">
      All customers that reopen their accounts with us before the <span class="hi">18<sup>th</sup> December</span> will be entered into our <span class="hi">FREE PRIZE</span> draw with the chance to win a 15" <span class="hi">LUMEN LAPTOP</span>.
    </div>

    <div class="contact">
      <p class="contact-label">For more information contact our office on</p>
      <p class="contact-phone">01632 960 418</p>
    </div>
  </main>
</body>
</html>
```